Business Card Design Project

I want my business cards to stand and feel timeless! I also want people to get their hands on them and freak out over how cool these are, I already have a logo i just want a very cool card design! this is for a makeup artist and maybe one day a line of cosmetics.

Target Market(s)

I want this to target women from 18 to 45

Industry/Entity Type

Business

Font styles to use
Decorative
Script

Colors

Designer to choose colors to be used in the design.

Requirements
Must have
• it must be elegante

```html
<!DOCTYPE html>
<html lang="en">
<head>
<meta charset="utf-8">
<title>Marielle Rose Makeup – Business Card</title>
<link rel="stylesheet" href="https://fonts.googleapis.com/css2?family=Lato:wght@300;400;700&display=swap">
<style>
  :root {
    --page-bg: #d9d9dc;
    --card-black: #050505;
    --logo-pink: #f3cbdb;
    --blush-start: #f8d6e6;
    --blush-end: #f6f4f9;
    --ink: #111111;
    --white: #ffffff;
  }
  * { margin: 0; padding: 0; box-sizing: border-box; }
  html, body {
    width: 1200px;
    height: 926px;
    overflow: hidden;
    background: var(--page-bg);
    font-family: "Lato", sans-serif;
  }
  .sheet {
    position: relative;
    width: 1200px;
    height: 926px;
  }
  .card {
    position: absolute;
    left: 250px;
    width: 700px;
    height: 400px;
    box-shadow: 0 10px 28px rgba(0, 0, 0, 0.22);
  }
  /* Front */
  .card-front {
    top: 48px;
    background: var(--card-black);
    display: flex;
    align-items: center;
    justify-content: center;
    padding: 0 60px;
  }
  .brand-name {
    color: var(--logo-pink);
    font-weight: 300;
    font-size: 32px;
    letter-spacing: 6px;
    text-transform: uppercase;
    white-space: nowrap;
    text-align: center;
  }
  /* Back */
  .card-back {
    top: 478px;
    background: linear-gradient(120deg, var(--blush-start) 0%, var(--blush-end) 75%);
  }
  .name-band {
    position: absolute;
    left: 0;
    top: 108px;
    width: 318px;
    height: 72px;
    background: var(--card-black);
    color: var(--white);
    padding: 12px 22px 0 0;
    text-align: right;
    box-shadow: 3px 4px 8px rgba(0, 0, 0, 0.35);
  }
  .person-name {
    font-size: 25px;
    font-weight: 300;
    line-height: 1.05;
    letter-spacing: 0.3px;
  }
  .person-name strong { font-weight: 700; }
  .person-role {
    font-size: 15px;
    font-weight: 400;
    letter-spacing: 1px;
    margin-top: 2px;
  }
  .contact-list {
    position: absolute;
    left: 352px;
    top: 118px;
    list-style: none;
    color: var(--ink);
    font-size: 19px;
    line-height: 1.2;
    letter-spacing: 0.4px;
  }
</style>
</head>
<body>
  <main class="sheet">
    <section class="card card-front" aria-label="Card front">
      <span class="brand-name">Marielle Rose Makeup</span>
    </section>

    <section class="card card-back" aria-label="Card back">
      <div class="name-band">
        <p class="person-name">YOUR <strong>FULLNAME</strong></p>
        <p class="person-role">FOUNDER</p>
      </div>
      <ul class="contact-list">
        <li>Mobile: +098 765 4321</li>
        <li>E-mail: yourname@web.com</li>
        <li>Web: www.websitiename.com</li>
      </ul>
    </section>
  </main>
</body>
</html>
```